New more attractive design for an old tired look that is high tech but inviting

Need a more modern eye catching design. We are and I/T and MSP and we need a new look. Need a call to action on each page. Needs to be in WordPress. Existing site is quorbelna.com. Needs to work on phones and tablets. The default home page should present us as an MSP/MSSP and direct the viewer to our services we offer.
Updates

Current deadline assigned at project inception has passed before project started

Need extra days to review

Target Market(s)

Our target market is other businesses. We do not target residential customers.

Industry/Entity Type

Business to Business oriented

Coding

Coded - Design and coding required

Number of Pages Required

5+ page

Font styles to use
Sans Serif

Requirements
Must have
• Must have a current relevant design with a call to action on each page.
Nice to have
• Dark background high tech look with people to make it attractive

```html
<!DOCTYPE html>
<html lang="en">
<head>
<meta charset="utf-8">
<title>Quorbelna Tech — Data Center Services</title>
<link href="https://fonts.googleapis.com/css2?family=Poppins:wght@400;500;600;700&display=swap" rel="stylesheet">
<style>
:root{
  --stage:#7a7a7a;
  --black:#000;
  --navy:#1b1e48;
  --navy-deep:#12143a;
  --navy-mid:#232a78;
  --indigo:#2b3490;
  --orange:#e8a84a;
  --white:#fff;
  --ink:#14163a;
  --muted:#8a8ca0;
  --rule:#9a9cb0;
  --link:#5aa8ff;
}
*{box-sizing:border-box;margin:0;padding:0}
html,body{width:1200px;height:1200px;overflow:hidden}
body{background:var(--stage);font-family:"Poppins",sans-serif;position:relative}
a,a:visited{color:inherit;text-decoration:none}
.page{position:absolute;left:416px;top:42px;width:1184px;height:3590px;transform:scale(.3108);transform-origin:0 0;background:var(--navy);overflow:hidden}
.accent{color:var(--orange)}
.btn{position:absolute;display:flex;align-items:center;justify-content:center;background:var(--orange);color:var(--white);border-radius:6px;font-weight:500;white-space:nowrap}
.btn-outline{background:transparent;border:3px solid var(--white)}
.brand{font-weight:700;color:var(--white);white-space:nowrap;display:flex;align-items:center;gap:10px}
.brand .dot{width:12px;height:12px;background:var(--white);border-radius:50%}

/* nav */
.nav{position:absolute;left:0;top:0;width:1184px;height:68px;background:var(--black)}
.nav .brand{position:absolute;left:130px;top:20px;font-size:22px}
.nav a,.nav a:visited{position:absolute;top:24px;font-size:14px;color:var(--white)}
.nav a.current,.nav a.current:visited{color:var(--orange);text-decoration:underline}
/* quote bar */
.quote{position:absolute;left:0;top:68px;width:1184px;height:80px;background:var(--navy)}
.quote .tick{position:absolute;left:134px;top:20px;width:40px;height:40px;border-radius:50%;background:var(--white);display:flex;align-items:center;justify-content:center}
.quote .lead{position:absolute;left:196px;top:22px;font-size:13px;color:var(--orange)}
.quote .sub{position:absolute;left:196px;top:40px;font-size:12px;color:var(--white)}
.quote .btn{left:814px;top:26px;width:150px;height:34px;font-size:11px;font-weight:600;border-radius:4px}
/* hero */
.hero{position:absolute;left:0;top:148px;width:1184px;height:452px;background:radial-gradient(ellipse at 75% 60%,#232a6e 0%,#15173e 55%,#0e1030 100%)}
.hero h1{position:absolute;left:122px;top:80px;font-size:72px;line-height:72px;letter-spacing:5px;color:var(--white);font-weight:700}
.hero p{position:absolute;left:122px;top:238px;width:490px;font-size:20px;line-height:30px;color:var(--white);letter-spacing:.5px}
.hero .btn{top:348px;height:36px;font-size:13px;font-weight:600}
.hero .tower{position:absolute;left:640px;top:60px;width:360px;height:392px;background:linear-gradient(160deg,#2a2d4a 0%,#14152a 60%,#0b0c1a 100%)}
.arrow{position:absolute;top:160px;width:40px;height:40px;border-radius:50%;background:var(--indigo);display:flex;align-items:center;justify-content:center}
/* data center */
.dc{position:absolute;left:0;top:600px;width:1184px;height:728px;background:var(--white);color:var(--ink)}
.dc .visual{position:absolute;left:124px;top:72px;width:360px;height:462px;border-radius:0 150px 0 0;background:linear-gradient(180deg,#05060d 0%,#0f1a3c 55%,#53627e 85%,#1b2030 100%)}
.dc h2{position:absolute;left:512px;top:60px;font-size:34px;font-weight:700}
.dc .intro{position:absolute;left:512px;top:108px;width:520px;font-size:18px;line-height:26px}
.feature{position:absolute;left:512px;width:560px}
.feature .ico{position:absolute;left:0;top:0;width:60px;height:60px;border-radius:50%;background:var(--navy-mid);display:flex;align-items:center;justify-content:center}
.feature h3{position:absolute;left:84px;top:0;font-size:22px;font-weight:600}
.feature p{position:absolute;left:88px;top:36px;width:460px;font-size:12.5px;line-height:19px}
.rule{position:absolute;left:524px;width:532px;height:2px;background:var(--rule)}
.dc .btn{left:512px;top:652px;width:318px;height:50px;font-size:16px}
/* services */
.services{position:absolute;left:0;top:1328px;width:1184px;height:1536px;background:radial-gradient(ellipse at 55% 58%,#2a34a0 0%,#1f2672 35%,#191c52 75%)}
.card{position:absolute;width:300px;height:240px;background:var(--white);border-radius:10px;text-align:center;color:var(--ink)}
.card .ico{position:absolute;left:124px;top:32px;width:52px;height:52px;border-radius:50%;background:var(--navy-mid);display:flex;align-items:center;justify-content:center}
.card.active .ico{left:120px;top:28px}
.card h4{position:absolute;left:10px;right:10px;top:96px;font-size:22px;font-weight:500;line-height:22px}
.card p{position:absolute;left:14px;right:14px;font-size:14.5px;line-height:22px;color:var(--muted)}
.card .go{position:absolute;right:18px;bottom:8px;width:22px;height:22px;border-radius:50%;background:#e3e3e8}
.card.active{border:4px solid var(--orange)}
.card.active .go{background:var(--orange)}
.card.lead{background:linear-gradient(135deg,#5b6090 0%,#2c3378 55%,#1a1f60 100%);text-align:left;color:var(--white)}
.card.lead small{position:absolute;left:26px;top:80px;font-size:13px;font-style:italic}
.card.lead strong{position:absolute;left:26px;top:100px;font-size:34px;font-weight:600}
.eyebrow{position:absolute;font-size:22px;font-weight:600;color:var(--orange)}
.sec-title{position:absolute;font-size:36px;line-height:48px;font-weight:700;color:var(--white)}
.sec-text{position:absolute;font-size:17px;line-height:26.5px;color:var(--white)}
.photo{position:absolute;border-radius:6px;box-shadow:0 0 18px rgba(140,150,255,.6)}
.services .btn{height:50px;font-size:16px}
/* cta */
.cta{position:absolute;left:0;top:2864px;width:1184px;height:292px;background:linear-gradient(180deg,#000 0%,#051510 60%,#0a2a22 100%)}
.cta h2{position:absolute;left:0;width:1184px;top:62px;text-align:center;font-size:34px;line-height:38px;font-weight:500;color:var(--white);letter-spacing:1px}
.cta .btn{top:204px;height:50px;font-size:16px}
/* footer */
.footer{position:absolute;left:0;top:3156px;width:1184px;height:434px;background:var(--navy);color:var(--white)}
.footer .brand{position:absolute;left:0;width:1184px;top:56px;justify-content:center;font-size:54px}
.footer .line{position:absolute;left:114px;width:962px;height:1px;background:#4a4e80}
.footer h5{font-size:15px;font-weight:600;margin-bottom:10px}
.footer .col{position:absolute;top:176px;font-size:14.5px;line-height:31px}
.footer .col ul{list-style:none}
.footer .about{position:absolute;left:114px;top:180px;width:300px;font-size:14.5px;line-height:25px}
.footer .social{position:absolute;top:326px;width:24px;height:24px;border-radius:50%;background:var(--white)}
.footer .news{position:absolute;left:874px;top:176px;width:202px;font-size:14.5px;line-height:25px}
.footer .field{position:absolute;left:874px;top:280px;width:202px;height:28px;background:#3a4066;font-size:9px;display:flex}
.footer .field span{flex:1;padding:8px 12px}
.footer .field b{background:#1a5a8a;font-weight:400;padding:8px 10px}
.footer .copy{position:absolute;left:0;width:1184px;top:390px;text-align:center;font-size:12px}
.footer .copy a,.footer .copy a:visited{color:var(--link);margin-left:10px}
</style>
</head>
<body>
<div class="page">

  <nav class="nav">
    <div class="brand"><span class="dot"></span>Quorbelna Tech</div>
    <a class="current" style="left:398px" href="#">Home</a>
    <a style="left:496px" href="#">Services &#8964;</a>
    <a style="left:616px" href="#">About Us</a>
    <a style="left:738px" href="#">Contact Us</a>
    <a style="left:868px" href="#">Community &amp; Resources</a>
  </nav>

  <div class="quote">
    <div class="tick"><svg width="22" height="22" viewBox="0 0 22 22"><path d="M5 11l4 4 8-8" fill="none" stroke="#1b1e48" stroke-width="3"/></svg></div>
    <div class="lead">Get a Quote for Your Data Center Needs.</div>
    <div class="sub">Let's have a conversation to see how we can help with your data center needs.</div>
    <div class="btn">Get a Free Consultation</div>
  </div>

  <section class="hero">
    <div class="arrow" style="left:6px"><svg width="14" height="14" viewBox="0 0 14 14"><path d="M9 2L4 7l5 5" fill="none" stroke="#5a7cff" stroke-width="2"/></svg></div>
    <div class="arrow" style="left:1138px"><svg width="14" height="14" viewBox="0 0 14 14"><path d="M5 2l5 5-5 5" fill="none" stroke="#5a7cff" stroke-width="2"/></svg></div>
    <h1>Data Center<br><span class="accent">Services</span></h1>
    <p>We offer colocation, virtualization, storage as a service and disaster recovery out of our own enterprise-grade data center.</p>
    <div class="btn" style="left:122px;width:102px">Services</div>
    <div class="btn btn-outline" style="left:244px;width:104px">Learn More</div>
    <div class="tower" role="img" aria-label="Dark high-rise data center building at night"></div>
  </section>

  <section class="dc">
    <div class="visual" role="img" aria-label="Glass cloud over server towers with a padlock"></div>
    <h2>Your <span class="accent">Data Center</span>, your way</h2>
    <p class="intro">From single colocated servers to fully redundant virtualized environments.</p>

    <div class="feature" style="top:204px">
      <div class="ico"><svg width="34" height="34" viewBox="0 0 34 34"><path d="M3 12l7-4 7 4 7-4 7 4v8l-7 6-7-5-7 5-7-6z" fill="#fff"/></svg></div>
      <h3>A True Partner</h3>
      <p>One size data center architecture does not fit all. We take the time to understand your specific requirements. We can provide as much or as little expertise as your organization requires for your specific project.</p>
    </div>
    <div class="rule" style="top:318px"></div>
    <div class="feature" style="top:350px">
      <div class="ico"><svg width="30" height="30" viewBox="0 0 30 30"><path d="M15 3l10 4v7c0 7-5 11-10 13C10 25 5 21 5 14V7z" fill="#fff"/><path d="M15 7l6 2.5v5c0 4-3 7-6 8.5z" fill="#232a78"/></svg></div>
      <h3>High Security</h3>
      <p>Our data center is a Tier III, standalone structure designed to withstand wind speeds up to 206mph. We have fully redundant power, cooling and internet connectivity. Biometrics are required to enter and visitors are always escorted.</p>
    </div>
    <div class="rule" style="top:478px"></div>
    <div class="feature" style="top:518px">
      <div class="ico"><svg width="30" height="30" viewBox="0 0 30 30"><path d="M24 5c-7 0-12 5-14 11l4 4c6-2 11-7 11-14z" fill="#fff"/><path d="M9 17l-4 1 3-6h4zM13 21l-1 4 6-3v-4zM8 21l-3 4 4-3z" fill="#fff"/></svg></div>
      <h3>Availability</h3>
      <p>The facility is powered by two separate utility feeds and a Ironvale diesel generator. We utilize multiple in-row cooling units, in-rack A/B power feeds and also have redundant, geographically diverse internet paths.</p>
    </div>
    <div class="btn">More About Data Center Services</div>
  </section>

  <section class="services">
    <div class="card lead" style="left:124px;top:46px" role="img" aria-label="Laptop on a desk with abstract screen art">
      <small>SERVICES</small><strong>OUR SERVICES</strong>
    </div>
    <div class="card" style="left:442px;top:46px">
      <div class="ico"><svg width="28" height="28" viewBox="0 0 30 30"><path d="M15 3l10 4v7c0 7-5 11-10 13C10 25 5 21 5 14V7z" fill="#fff"/><path d="M15 7l6 2.5v5c0 4-3 7-6 8.5z" fill="#232a78"/></svg></div>
      <h4>Cybersecurity</h4>
      <p style="top:146px">Enterprise-grade cybersecurity without the enterprise price tag.</p>
      <span class="go"></span>
    </div>
    <div class="card" style="left:760px;top:46px">
      <div class="ico"><svg width="28" height="28" viewBox="0 0 28 28"><path d="M3 11a16 16 0 0 1 22 0M7 15a10 10 0 0 1 14 0M11 19a4 4 0 0 1 6 0" fill="none" stroke="#fff" stroke-width="3" stroke-linecap="round"/><circle cx="14" cy="23" r="2" fill="#fff"/></svg></div>
      <h4>Managed Networks<br>for MDUs</h4>
      <p style="top:146px">Essential high speed Wi-Fi for student housing fast, reliable, and ready for all devices, 24/7.</p>
      <span class="go"></span>
    </div>
    <div class="card" style="left:124px;top:304px">
      <div class="ico"><svg width="26" height="26" viewBox="0 0 26 26"><rect x="3" y="4" width="20" height="8" rx="2" fill="#fff"/><rect x="3" y="14" width="20" height="8" rx="2" fill="#fff"/><circle cx="19" cy="8" r="1.3" fill="#232a78"/><circle cx="19" cy="18" r="1.3" fill="#232a78"/></svg></div>
      <h4>Data Center Services</h4>
      <p style="top:128px">VaultFrame® Colocation &amp; Virtualization: Tailored data center solutions to keep your business data secure and always available.</p>
      <span class="go"></span>
    </div>
    <div class="card" style="left:442px;top:304px">
      <div class="ico"><svg width="26" height="26" viewBox="0 0 26 26"><path d="M9 3v6M17 3v6" stroke="#fff" stroke-width="3"/><path d="M6 9h14v4a7 7 0 0 1-14 0z" fill="#fff"/><path d="M13 20v4" stroke="#fff" stroke-width="3"/></svg></div>
      <h4>Low Voltage Wiring</h4>
      <p style="top:128px">Structured cabling for voice data/AV - installed to industry stadards with lifetime warranty.</p>
      <span class="go"></span>
    </div>
    <div class="card active" style="left:760px;top:304px">
      <div class="ico"><svg width="26" height="26" viewBox="0 0 26 26"><path d="M5 15v-3a8 8 0 0 1 16 0v3" fill="none" stroke="#fff" stroke-width="3"/><rect x="3" y="14" width="6" height="8" rx="2" fill="#fff"/><rect x="17" y="14" width="6" height="8" rx="2" fill="#fff"/></svg></div>
      <h4>Office IT Support</h4>
      <p style="top:124px">Complete IT solutions: Managed services, on-demand support, and 24/7 security for seamless, secure operations.</p>
      <span class="go"></span>
    </div>

    <div class="eyebrow" style="left:122px;top:662px">Our Company</div>
    <h2 class="sec-title" style="left:124px;top:694px">About Quorbelna<br>Tech</h2>
    <p class="sec-text" style="left:122px;top:804px;width:370px">Founded in 1995 in Harlow Ridge, Quorbelna Tech began as a side project by ex-Valewright Power IT experts Marrow &amp; Pell. By 2000, they went full-time to expand their tech services.</p>
    <div class="btn" style="left:126px;top:952px;width:250px">Read Our Founder's Story</div>
    <div class="photo" style="left:570px;top:752px;width:466px;height:250px;background:linear-gradient(135deg,#c9c4c8 0%,#6b6f88 45%,#3a3f58 100%)" role="img" aria-label="Team of colleagues smiling at laptops in a bright office"></div>

    <div class="photo" style="left:128px;top:1132px;width:466px;height:250px;background:linear-gradient(180deg,#0c1238 0%,#1d2a6a 50%,#0a0d28 100%)" role="img" aria-label="Audience seated at a technology conference"></div>
    <h2 class="sec-title" style="left:656px;top:1132px;line-height:40px">Transform your<br>business with the<br>IT community</h2>
    <p class="sec-text" style="left:654px;top:1264px;width:414px">Supercharge your data center with Peerline Network—learn proven strategies from top MSPs to optimize security, scalability, and performance through peer insights and expert guidance.</p>
    <div class="btn" style="left:656px;top:1376px;width:158px">Explore More</div>
  </section>

  <section class="cta" role="img" aria-label="Glowing data city skyline backdrop">
    <h2>Everything you need to<br><span class="accent">run and grow</span> your <span class="accent">MSP/MSSP</span> in<br>a single platform</h2>
    <div class="btn" style="left:414px;width:158px">555-014-2270</div>
    <div class="btn" style="left:610px;width:160px;background:transparent;border:3px solid var(--orange);color:var(--orange)">Explore More</div>
  </section>

  <footer class="footer">
    <div class="brand"><span class="dot" style="width:18px;height:18px"></span>Quorbelna Tech</div>
    <div class="line" style="top:154px"></div>
    <p class="about">Lorem ipsum dolor sit amet, consectetuer adipiscing elit, sed diam nonummy nibh euismod tincidunt ut laoreet dolore magna aliquam erat volutpat. lamcorper</p>
    <span class="social" style="left:120px"></span>
    <span class="social" style="left:202px"></span>
    <span class="social" style="left:284px"></span>
    <span class="social" style="left:362px"></span>
    <div class="col" style="left:460px"><h5>Quick Links</h5><ul><li>Home</li><li>Services</li><li>About Us</li><li>Comunity &amp; resource</li><li>Contact</li></ul></div>
    <div class="col" style="left:652px"><h5>Information</h5><ul><li>Get a quote</li><li>Office IT Support</li><li>Privacy Policy</li><li>Terms &amp; Conditions</li></ul></div>
    <div class="news"><h5>Newsletter</h5>Subscribe to receive updates, access to exclusive offers, and more.</div>
    <div class="field"><span>Email</span><b>Submit</b></div>
    <div class="line" style="top:364px"></div>
    <div class="copy">2025 © Quorbelna Tech, Inc., All Rights Reserved. <a href="#">Privacy Policy</a><a href="#">Terms of Use</a><a href="#">Cookie Policy</a></div>
  </footer>

</div>
</body>
</html>
```